Business Card Design for Varnok Facility Services

We are looking for a Business Card Design for the Company "Varnok Facility Services."
Front side:
- Company Logo (small)
- Company Name, address, pohone, website and personal data.
- white background, for text e.g. company colors (blue or green like in the logo)
Please use following data:
Company data:
Varnok Facility Services Tulbrecht
Kirchmattweg 12
6331 Cham
www.varnok-fs.ch
Person data:
Ruben Tulbrecht
Geschäftsführer
+41 76 519 84 60
info@varnok-fs.ch
Back side:
could be colored in blue or green
please use a big logo sing and some smaller icons to say what is all beeing offered in facility services, like cleaning, maintenance cleaning
industrial cleaning, caretaking, gardening, disposal. There is no need for everyone of the icons if there are similar or an icon is standing for more of them.
Cleaning Service
colors to use:
blue: HEX 246BB0
green: HEX 52B33E

```html
<!DOCTYPE html>
<html lang="de">
<head>
<meta charset="utf-8">
<title>Varnok Facility Services – Visitenkarte</title>
<link rel="stylesheet" href="https://fonts.googleapis.com/css2?family=Poppins:wght@400;500;600&display=swap">
<style>
  :root {
    --brand-blue: #0b52ae;
    --card-blue: #0451b0;
    --brand-green: #52b33e;
    --icon-green: #7cc242;
    --text-grey: #555555;
    --divider: #9a9a9a;
    --paper: #ffffff;
    --backdrop: #ebe8e4;
  }
  * { margin: 0; padding: 0; box-sizing: border-box; }
  html, body { width: 1125px; height: 1200px; overflow: hidden; }
  body {
    background: var(--backdrop);
    font-family: "Poppins", sans-serif;
    position: relative;
  }
  .card {
    position: absolute;
    left: 150px;
    width: 825px;
    height: 471px;
    box-shadow: 0 3px 8px rgba(0,0,0,0.25);
  }
  .card-front { top: 98px; background: var(--paper); }
  .card-back { top: 632px; background: var(--card-blue); }

  .person { position: absolute; right: 425px; top: 203px; text-align: right; }
  .person-name { color: var(--brand-blue); font-weight: 600; font-size: 31px; line-height: 1.1; }
  .person-role { color: var(--brand-green); font-size: 21px; line-height: 1.2; }

  .divider {
    position: absolute; left: 426px; top: 184px;
    width: 1px; height: 103px; background: var(--divider);
  }

  .contact-list { position: absolute; left: 455px; top: 194px; list-style: none; }
  .contact-item {
    display: flex; align-items: center; gap: 8px;
    color: var(--text-grey); font-size: 20px; line-height: 26.5px;
  }
  .contact-item svg { width: 19px; height: 19px; flex: none; fill: var(--brand-blue); }

  .address {
    position: absolute; left: 58px; top: 400px;
    display: flex; align-items: center; gap: 6px;
    color: var(--text-grey); font-size: 20px;
  }
  .address svg { width: 17px; height: 23px; fill: var(--brand-blue); }

  .brand {
    position: absolute; left: 0; right: 0; top: 150px;
    display: flex; justify-content: center; align-items: center; gap: 18px;
  }
  .brand-dot { width: 44px; height: 44px; border-radius: 50%; background: var(--paper); }
  .brand-name { color: var(--paper); font-weight: 600; font-size: 42px; letter-spacing: 1px; }

  .services {
    position: absolute; top: 312px; left: 0; width: 825px; list-style: none;
  }
  .service {
    position: absolute; width: 140px; margin-left: -70px;
    text-align: center; color: var(--icon-green); font-size: 17px; line-height: 21px;
  }
  .service-icon {
    width: 78px; height: 78px; margin: 0 auto 9px;
    border: 2.5px solid var(--icon-green); border-radius: 50%;
    display: flex; align-items: center; justify-content: center;
  }
  .service-icon span {
    width: 38px; height: 38px; border-radius: 50%; background: var(--icon-green);
  }
</style>
</head>
<body>
  <section class="card card-front" aria-label="Vorderseite">
    <div class="person">
      <p class="person-name">Ruben Tulbrecht</p>
      <p class="person-role">Geschäftsführer</p>
    </div>
    <div class="divider"></div>
    <ul class="contact-list">
      <li class="contact-item">
        <svg viewBox="0 0 20 20" aria-hidden="true"><path d="M6 1h8a2 2 0 0 1 2 2v14a2 2 0 0 1-2 2H6a2 2 0 0 1-2-2V3a2 2 0 0 1 2-2zm0 2.5v11h8v-11zm4 12.2a1 1 0 1 0 0 2 1 1 0 0 0 0-2z"/></svg>
        +41 76 519 84 60
      </li>
      <li class="contact-item">
        <svg viewBox="0 0 20 20" aria-hidden="true"><path d="M2 5h16v11H2zm1.5 1.5v.4L10 11l6.5-4.1v-.4zm0 2.2v5.8h13V8.7L10 12.8z"/></svg>
        info@varnok-fs.ch
      </li>
      <li class="contact-item">
        <svg viewBox="0 0 20 20" aria-hidden="true"><circle cx="10" cy="10" r="9"/><path d="M5 6c2 0 3 1 3 2.5S6 10 7 12s2 3 1 5M13 3c-1 2 1 3 2 3.5s2 3 0 5-1 4-2 5" stroke="#fff" stroke-width="1.3" fill="none"/></svg>
        www.varnok-fs.ch
      </li>
    </ul>
    <p class="address">
      <svg viewBox="0 0 17 23" aria-hidden="true"><path d="M8.5 0A8.5 8.5 0 0 0 0 8.5C0 15 8.5 23 8.5 23S17 15 17 8.5A8.5 8.5 0 0 0 8.5 0zm0 4.5a4 4 0 1 1 0 8 4 4 0 0 1 0-8z"/></svg>
      Varnok Facility Services Tulbrecht | Kirchmattweg 12, 6331 Cham
    </p>
  </section>

  <section class="card card-back" aria-label="Rückseite">
    <div class="brand">
      <span class="brand-dot"></span>
      <span class="brand-name">Varnok Facility Services</span>
    </div>
    <ul class="services">
      <li class="service" style="left:105px"><div class="service-icon" role="img" aria-label="Besen-Symbol"><span></span></div>Cleaning</li>
      <li class="service" style="left:224px"><div class="service-icon" role="img" aria-label="Hauswart-Symbol"><span></span></div>Caretaking</li>
      <li class="service" style="left:359px"><div class="service-icon" role="img" aria-label="Handschuh-Symbol"><span></span></div>Maintenance<br>cleaning</li>
      <li class="service" style="left:486px"><div class="service-icon" role="img" aria-label="Wischmopp-Symbol"><span></span></div>Industrial<br>cleaning</li>
      <li class="service" style="left:604px"><div class="service-icon" role="img" aria-label="Giesskannen-Symbol"><span></span></div>Gardening</li>
      <li class="service" style="left:719px"><div class="service-icon" role="img" aria-label="Abfalleimer-Symbol"><span></span></div>Disposal</li>
    </ul>
  </section>
</body>
</html>
```